Need Business Cards, Letterhead, and Stationary

Hi, please design a full stationary set for the attached logo (Business Cards, Letterhead, A4 Envelope, and other important stationary items that you can think of)
Please be as creative as you wish. The logo is for An Entrepreneurship Academy that teaches young and starting Entrepreneur skills they need to start their business.

```html
<!DOCTYPE html>
<html lang="en">
<head>
<meta charset="utf-8">
<title>Kestrel Founders Academy – Stationery Set</title>
<link href="https://fonts.googleapis.com/css2?family=Lato:wght@400;700;900&display=swap" rel="stylesheet">
<style>
  :root{
    --brand-blue:#1673ad;
    --brand-yellow:#f9c80e;
    --brand-gray:#6f6f72;
    --brand-black:#121212;
    --ink:#2b2b2b;
    --paper:#ffffff;
    --rule:#d6d6d6;
    --board-light:#b4b5b8;
    --board-dark:#6b6c6f;
  }
  *{box-sizing:border-box;margin:0;padding:0}
  html,body{width:1169px;height:1200px;overflow:hidden}
  body{
    font-family:"Lato",sans-serif;color:var(--ink);
    background:radial-gradient(ellipse 60% 55% at 62% 45%,var(--board-light),var(--board-dark) 85%);
    position:relative;
  }
  .sheet{position:absolute;background:var(--paper);box-shadow:0 1px 3px rgba(0,0,0,.25)}

  /* wordmark */
  .wordmark{display:flex;align-items:center;gap:6px}
  .wordmark-dot{border-radius:50%;background:var(--brand-blue);flex:none}
  .wordmark-name{font-weight:900;color:#3a3a3c;letter-spacing:.5px;line-height:1}

  .chevron-strip{position:absolute;background:linear-gradient(90deg,var(--brand-gray),var(--brand-blue),var(--brand-yellow),var(--brand-black),var(--brand-gray),var(--brand-blue),var(--brand-yellow),var(--brand-black))}

  .color-bars{position:absolute;display:flex}
  .color-bars span{flex:1}
  .bar-black{background:var(--brand-black)}
  .bar-blue{background:var(--brand-blue)}
  .bar-yellow{background:var(--brand-yellow)}

  .contact-list{list-style:none}
  .contact-list li{display:flex;align-items:flex-start;gap:5px}
  .contact-list svg{flex:none;fill:var(--brand-blue)}

  /* letterhead */
  .letterhead{left:79px;top:39px;width:592px;height:766px}
  .letterhead .top-band{position:absolute;left:0;top:0;width:412px;height:25px;background:var(--brand-blue)}
  .letterhead .chevron-strip{left:412px;top:0;width:172px;height:25px;clip-path:polygon(8% 0,100% 0,100% 100%,8% 100%,0 50%)}
  .letterhead .wordmark{position:absolute;left:40px;top:48px}
  .letterhead .contact-list{position:absolute;left:481px;top:45px;font-size:7px;line-height:11px}
  .letterhead .footer-rule{position:absolute;left:0;right:0;top:730px;border-top:1px solid var(--rule)}
  .letterhead .footer-text{position:absolute;left:0;right:0;top:733px;text-align:center;font-size:8.5px}
  .letterhead .footer-text span{margin:0 8px}
  .letterhead .color-bars{left:0;right:0;bottom:0;height:10px}

  /* envelope */
  .envelope{left:71px;top:823px;width:689px;height:340px}
  .envelope .top-band{position:absolute;left:0;top:20px;width:510px;height:31px;background:var(--brand-blue)}
  .envelope .chevron-strip{left:505px;top:20px;width:174px;height:31px;clip-path:polygon(8% 0,100% 0,100% 100%,8% 100%,0 50%)}
  .envelope .wordmark{position:absolute;left:44px;top:96px}
  .envelope .org-name{position:absolute;left:44px;top:140px;font-size:8.5px}
  .envelope .contact-list{position:absolute;left:44px;top:153px;font-size:8.5px;line-height:11px}
  .envelope .color-bars{left:0;right:0;top:1294px;top:294px;height:10px}

  /* business card front */
  .card-front{left:704px;top:243px;width:367px;height:209px;overflow:hidden}
  .card-front .wordmark{position:absolute;left:24px;top:74px}
  .card-front .org-name{position:absolute;left:24px;top:128px;font-size:11px}
  .card-front .contact-list{position:absolute;left:24px;top:144px;font-size:10.5px;line-height:13px}
  .card-front .chevron-art{position:absolute;left:248px;top:43px;width:119px;height:122px;
    background:linear-gradient(90deg,var(--brand-gray) 0 30%,var(--brand-blue) 30% 65%,var(--brand-yellow) 65%);
    clip-path:polygon(35% 0,100% 0,100% 100%,35% 100%,0 50%)}

  /* business card back */
  .card-back{left:704px;top:529px;width:367px;height:208px;background:var(--brand-blue);color:#fff;overflow:hidden}
  .card-back .emblem-area{position:absolute;left:0;top:0;width:82px;height:208px;background:linear-gradient(90deg,rgba(255,255,255,.9),rgba(255,255,255,.55))}
  .card-back .person-name{position:absolute;left:187px;top:17px;font-size:21px;font-weight:400;letter-spacing:.8px}
  .card-back .person-role{position:absolute;left:188px;top:44px;font-size:10px}
  .card-back .contact-list{position:absolute;left:101px;top:161px;font-size:11px;line-height:14px}
  .card-back .contact-list svg{fill:#fff}
</style>
</head>
<body>

<!-- Letterhead -->
<section class="sheet letterhead">
  <div class="top-band"></div>
  <div class="chevron-strip" role="img" aria-label="Row of multicoloured chevron arrows"></div>
  <div class="wordmark">
    <span class="wordmark-dot" style="width:26px;height:26px"></span>
    <span class="wordmark-name" style="font-size:28px">KESTREL</span>
  </div>
  <ul class="contact-list">
    <li><svg width="6" height="8" viewBox="0 0 6 8"><rect x="1" y="0" width="4" height="8" rx="1"/></svg>0-000-000-0000</li>
    <li><svg width="6" height="8" viewBox="0 0 6 8"><circle cx="3" cy="2" r="2"/><rect x="0" y="5" width="6" height="3" rx="1.5"/></svg>jordan@mailbox.com</li>
    <li><svg width="6" height="8" viewBox="0 0 6 8"><circle cx="3" cy="4" r="3"/></svg>www.website.com</li>
  </ul>
  <div class="footer-rule"></div>
  <p class="footer-text"><span>www.website.com.</span><span>Address: 2/114Lorem Ipsum.</span></p>
  <div class="color-bars"><span class="bar-black"></span><span class="bar-blue"></span><span class="bar-yellow"></span><span class="bar-black"></span></div>
</section>

<!-- Business card front -->
<section class="sheet card-front">
  <div class="wordmark">
    <span class="wordmark-dot" style="width:30px;height:30px"></span>
    <span class="wordmark-name" style="font-size:30px">KESTREL</span>
  </div>
  <p class="org-name">Kestrel Founders Academy</p>
  <ul class="contact-list">
    <li><svg width="9" height="9" viewBox="0 0 9 9"><circle cx="4.5" cy="4.5" r="4.5"/></svg>www.website.com</li>
    <li><svg width="9" height="9" viewBox="0 0 9 9"><path d="M0 2h9v6H0z"/></svg>00 Dummy Text Road<br>Dummy 0000, Country</li>
  </ul>
  <div class="chevron-art" role="img" aria-label="Large layered chevron shape in gray, blue and yellow"></div>
</section>

<!-- Business card back -->
<section class="sheet card-back">
  <div class="emblem-area" role="img" aria-label="Large white brand emblem cropped at the left edge"></div>
  <h2 class="person-name">Jordan Lee</h2>
  <p class="person-role">Managing Director</p>
  <ul class="contact-list">
    <li><svg width="7" height="10" viewBox="0 0 7 10"><rect x="1" y="0" width="5" height="10" rx="1"/></svg>0-000-000-0000</li>
    <li><svg width="8" height="10" viewBox="0 0 8 10"><circle cx="4" cy="3" r="2.5"/><rect x="0" y="6" width="8" height="4" rx="2"/></svg>jordan@mailbox.com</li>
  </ul>
</section>

<!-- Envelope -->
<section class="sheet envelope">
  <div class="top-band"></div>
  <div class="chevron-strip" role="img" aria-label="Row of multicoloured chevron arrows"></div>
  <div class="wordmark">
    <span class="wordmark-dot" style="width:26px;height:26px"></span>
    <span class="wordmark-name" style="font-size:27px">KESTREL</span>
  </div>
  <p class="org-name">Kestrel Founders Academy</p>
  <ul class="contact-list">
    <li><svg width="6" height="8" viewBox="0 0 6 8"><rect x="1" y="0" width="4" height="8" rx="1"/></svg>0-000-000-0000</li>
    <li><svg width="6" height="8" viewBox="0 0 6 8"><circle cx="3" cy="2" r="2"/><rect x="0" y="5" width="6" height="3" rx="1.5"/></svg>jordan@mailbox.com</li>
    <li><svg width="6" height="8" viewBox="0 0 6 8"><circle cx="3" cy="4" r="3"/></svg>www.website.com</li>
    <li><svg width="7" height="8" viewBox="0 0 7 8"><path d="M0 2h7v5H0z"/></svg>00 Dummy Text Road<br>Dummy 0000, Country</li>
  </ul>
  <div class="color-bars"><span class="bar-black"></span><span class="bar-blue"></span><span class="bar-yellow"></span><span class="bar-black"></span></div>
</section>

</body>
</html>
```